BHP Business Cards

I need business cards for "copper glen partners llc" doublesided... logo on the back (also include logo on front)
logo attached to project... i have jpg up.. let me know if you need eps file.
Company Info:
842 East Marlow Avenue, Suite 7B
Chicago, Illinois 60617
facsimile 312-555-4186 (list fax, address, website on all cards.)
www.copperglenpartnersllc.example
Three different people on cards:
Dorian K. Patel, CPA MST
Principal
ofc 312-555-0271
mobile 312-555-0388
doriankpatel@copperglenpartnersllc.example
Harold J. Quenby, CPA MST
Principal
haroldjquenby@copperglenpartnersllc.example
mobile 708-555-0149
ofc 312-555-0271
Miles T Carver
Principal
ofc 312-555-0271
no mobile
milestcarver@copperglenpartnersllc.example
I have multiple projects listed.. see below:
Business cards for copper glen partners llc
letterhead
envelopes
Business cards for KM Holdings LLC
letterhead
envelopes
rich people
Business

```html
<!DOCTYPE html>
<html lang="en">
<head>
<meta charset="utf-8">
<title>Copper Glen Partners LLC — Business Card</title>
<link rel="stylesheet" href="https://fonts.googleapis.com/css2?family=Cinzel:wght@400;600&family=Open+Sans:wght@400&display=swap">
<style>
  :root {
    --brand-blue: #1d4a86;
    --band-fade: #8e9dc6;
    --card-white: #ffffff;
    --ink: #2b3440;
    --backdrop: #e8e5e0;
  }
  * { box-sizing: border-box; margin: 0; padding: 0; }
  html, body { width: 1200px; height: 1044px; overflow: hidden; }
  body {
    background: var(--backdrop);
    position: relative;
    font-family: "Open Sans", sans-serif;
  }
  .card {
    position: absolute;
    left: 180px;
    width: 840px;
    height: 480px;
    overflow: hidden;
    box-shadow: 0 6px 18px rgba(0,0,0,0.18);
  }
  .card-front { top: 22px; background: var(--card-white); }
  .card-back { top: 542px; background: var(--brand-blue); }

  .header-band {
    position: absolute; left: 0; top: 0; width: 840px; height: 190px;
    background: linear-gradient(180deg,
      var(--brand-blue) 0%,
      var(--brand-blue) 66%,
      var(--band-fade) 84%,
      var(--card-white) 100%);
  }
  .holder { position: absolute; left: 60px; top: 34px; color: var(--card-white); }
  .holder-name {
    font-family: "Cinzel", serif; font-weight: 600;
    font-size: 31px; letter-spacing: 0.5px; white-space: nowrap;
  }
  .holder-title {
    font-family: "Cinzel", serif; font-weight: 400;
    font-size: 20px; margin-top: 2px; letter-spacing: 0.5px;
  }
  .company-name {
    position: absolute; right: 52px; top: 290px;
    font-family: "Cinzel", serif; font-weight: 600;
    font-size: 36px; color: var(--brand-blue);
    letter-spacing: 0.5px; white-space: nowrap;
  }
  .phone-list { position: absolute; left: 48px; top: 380px; list-style: none; }
  .phone-list li {
    display: flex; align-items: center; gap: 10px;
    font-size: 18px; color: var(--ink); height: 31px;
  }
  .phone-icon { width: 18px; height: 18px; }
  .company-contact {
    position: absolute; right: 52px; top: 382px;
    text-align: right; font-size: 17px; color: var(--ink); line-height: 1;
  }
  .company-contact .address { margin-bottom: 20px; }
  .company-contact .email { margin-bottom: 9px; }

  .back-mark {
    position: absolute; left: 0; right: 0; top: 190px;
    text-align: center;
    font-family: "Cinzel", serif; font-weight: 600;
    font-size: 50px; color: var(--card-white); letter-spacing: 1px; white-space: nowrap;
  }
  .back-website {
    position: absolute; left: 0; right: 0; top: 360px;
    text-align: center; font-size: 17px; letter-spacing: 3px;
    color: var(--card-white);
  }
</style>
</head>
<body>
  <section class="card card-front">
    <div class="header-band" role="img" aria-label="Blue header band with decorative ribbon"></div>

    <div class="holder">
      <p class="holder-name">Dorian K. Patel, CPA MST</p>
      <p class="holder-title">Principal</p>
    </div>

    <p class="company-name">Copper Glen Partners llc</p>

    <ul class="phone-list">
      <li>
        <svg class="phone-icon" viewBox="0 0 18 18" aria-hidden="true"><circle cx="9" cy="9" r="9" fill="var(--brand-blue)"/><path d="M6 5 L8 5 L8.6 7.2 L7.6 8 C8.2 9.2 8.8 9.8 10 10.4 L10.8 9.4 L13 10 L13 12 C9 12.4 5.6 9 6 5 Z" fill="#fff"/></svg>
        <span>312-555-0271</span>
      </li>
      <li>
        <svg class="phone-icon" viewBox="0 0 18 18" aria-hidden="true"><circle cx="9" cy="9" r="9" fill="var(--brand-blue)"/><rect x="6.5" y="4" width="5" height="10" rx="1" fill="#fff"/><rect x="7.3" y="5.2" width="3.4" height="6" fill="var(--brand-blue)"/></svg>
        <span>312-555-0388</span>
      </li>
      <li>
        <svg class="phone-icon" viewBox="0 0 18 18" aria-hidden="true"><circle cx="9" cy="9" r="9" fill="var(--brand-blue)"/><rect x="5" y="8" width="8" height="5" fill="#fff"/><rect x="6.5" y="4.5" width="5" height="4" fill="#fff"/></svg>
        <span>312-555-4186</span>
      </li>
    </ul>

    <div class="company-contact">
      <p class="address">842 East Marlow Avenue, Suite 7B, Chicago, Illinois 60617</p>
      <p class="email">E: doriankpatel@copperglenpartnersllc.example</p>
      <p class="website">www.copperglenpartnersllc.example</p>
    </div>
  </section>

  <section class="card card-back">
    <p class="back-mark">Copper Glen Partners llc</p>
    <p class="back-website">www.copperglenpartnersllc.example</p>
  </section>
</body>
</html>
```